Wordpress Design Project plorn.ie

We want to setup a new WP site for a VANTERLY USER group in Ireland. We hae the logo and a short intro video
We want to be able to blog and post videos (u tube links) to the page.

If you look at the image below *plorn site this is a try we made, but have run out of time.

Target Market(s)

Techies and mostly bouring men like us.

Industry/Entity Type

Group

Requirements
Must have
• 4 pages, Simple Clean and easy to nivagate and easy for us to use.

Explore
Plan
Deploy
Configure

have a look at - http://www.plorn.be/ We do not want an exact copy of
Nice to have
• Login
down load section
link to other blogs etc
social netwrok links FB,Pintrest etc
about us

```html
<!DOCTYPE html>
<html lang="en">
<head>
<meta charset="utf-8">
<title>plorn.ie – Fleet Console User Group Ireland</title>
<link rel="stylesheet" href="https://fonts.googleapis.com/css2?family=Oswald:wght@400;500&family=Roboto+Condensed:wght@400;700&family=Arimo:ital,wght@0,400;0,700;1,400&display=swap">
<style>
:root{
  --dark:#2f2f2f;
  --dark2:#444;
  --green:#3f9a1e;
  --green-dark:#256b0e;
  --green-light:#6cc23a;
  --orange:#f6a21b;
  --text:#444;
  --muted:#777;
  --light:#ededed;
  --band:#e4e4e4;
  --link:#1f7fae;
  --white:#fff;
}
*{box-sizing:border-box;margin:0;padding:0}
html,body{width:971px;height:1200px;overflow:hidden;background:var(--light)}
body{font-family:"Arimo",Arial,sans-serif;color:var(--text)}
.page{position:relative;width:1000px;height:1236px;transform:scale(.971);transform-origin:0 0;background:var(--light)}
.abs{position:absolute}
.header-bg{left:0;top:0;width:1000px;height:440px;background:radial-gradient(ellipse at 50% 30%,#4a4a4a,#262626 80%)}
.logo{left:70px;top:2px;width:302px;height:125px;background:var(--white);border:2px solid #d8d8d8;padding:18px 14px}
.logo-name{font-family:"Arimo",sans-serif;font-size:38px;line-height:36px;color:#111;letter-spacing:1px}
.logo-sub{font-family:"Arimo",sans-serif;font-size:22px;line-height:24px;color:#111}
.logo-sub.green{color:var(--green)}
.logo-mark{left:238px;top:24px;width:44px;height:44px;background:var(--green-light)}
.account{left:665px;top:2px;width:158px;height:34px;background:#262626;border-radius:0 0 6px 6px;display:flex;font-family:"Roboto Condensed",sans-serif;font-size:16px;color:#bbb}
.account span{flex:1;text-align:center;line-height:34px}
.account span+span{border-left:1px solid #444}
.phone{left:838px;top:12px;display:flex;align-items:center;gap:6px;font-family:"Roboto Condensed",sans-serif;font-size:18px;color:#ccc}
.search{left:676px;top:52px;width:284px;height:21px;background:#222;border:1px solid #4a4a4a;border-radius:3px;font-size:12px;color:#888;padding:3px 8px}
.search svg{position:absolute;right:6px;top:4px}
.nav{left:0;top:83px;width:1000px;height:45px}
.nav-bar{left:20px;top:0;width:960px;height:45px;background:linear-gradient(#5cb82f,#2f8a14);box-shadow:0 2px 4px rgba(0,0,0,.4)}
.nav ul{position:absolute;left:420px;top:6px;list-style:none;display:flex;gap:0}
.nav li{font-family:"Oswald",sans-serif;font-size:17px;color:var(--white);padding:0 22px;line-height:32px;text-transform:uppercase}
.nav li.active{background:linear-gradient(#ffc43d,var(--orange));color:#222;border-radius:3px;padding:0 13px;margin-right:15px;border:1px solid #c77d0a}
.slider{left:38px;top:128px;width:922px;height:374px;border:3px solid var(--green);border-top:none;border-radius:0 0 14px 14px;overflow:hidden}
.slider-photo{width:100%;height:100%;background:linear-gradient(100deg,#3b4a5a 0%,#b8b4ab 35%,#e6e2dc 50%,#6e7a84 70%,#2c3440 100%)}
.arrow{width:44px;height:44px;border-radius:50%;background:radial-gradient(circle at 40% 35%,#e6e6e6,#8a8a8a);border:2px solid #ddd;display:flex;align-items:center;justify-content:center}
.cards{left:65px;top:455px}
.card{position:absolute;top:0;width:195px;height:150px;background:linear-gradient(#5c5c5c,#a9a9a9 60%,#d4d4d4);border:2px solid #e6e6e6;border-radius:3px;overflow:hidden;padding:10px 12px}
.card-photo{position:absolute;right:-2px;top:-2px;width:120px;height:112px;border-radius:0 0 0 100%;background:linear-gradient(140deg,#8aa0b6,#3b4d63)}
.card h3{position:relative;font-family:"Oswald",sans-serif;font-weight:500;font-size:20px;color:var(--white);line-height:24px}
.card .sub{position:relative;font-family:"Roboto Condensed",sans-serif;font-weight:700;font-size:17px;line-height:25px;color:var(--white);margin-top:6px}
.card p{position:relative;font-size:12px;color:#222;margin-top:4px}
.card a{position:relative;display:block;font-size:12px;color:var(--green-light);text-decoration:underline;margin-top:7px}
.news{left:40px;top:658px;width:430px}
.news p{margin-left:53px;font-size:12px;line-height:18px;color:var(--text);margin-bottom:17px}
.news b{color:var(--green-dark)}
.btn{display:inline-block;font-family:"Roboto Condensed",sans-serif;font-weight:700;font-size:13px;color:var(--white);background:linear-gradient(#3fa11c,#1f6b0a);border-radius:4px;border:1px solid #175606;text-transform:uppercase;text-align:center}
.demo{left:548px;top:658px;width:393px}
.demo h2{font-family:"Oswald",sans-serif;font-weight:400;font-size:20px;color:#222;padding-bottom:6px;border-bottom:1px solid #bbb}
.demo .quote{font-style:italic;font-size:12px;line-height:18px;color:var(--muted);margin-top:14px}
.demo p{font-size:12px;line-height:18px;color:var(--text);margin-top:12px}
.band{left:0;top:886px;width:1000px;height:274px;background:var(--band);border-top:2px solid #d6d6d6;border-bottom:1px solid #d0d0d0}
.col-head{display:flex;align-items:center;gap:10px;font-family:"Oswald",sans-serif;font-size:19px;color:var(--green);text-transform:uppercase;border-bottom:1px solid #ccc;padding-bottom:6px;height:46px}
.blogs{left:42px;top:892px;width:278px}
.blog-item{display:flex;gap:12px;margin:14px 0 0 12px;height:31px}
.avatar{width:30px;height:30px;border-radius:50%;background:radial-gradient(circle,#e8c35a,#a27d1c);border:2px solid #fff}
.blog-item b{display:block;font-family:"Roboto Condensed",sans-serif;font-size:14px;color:#333}
.blog-item span{font-size:11px;color:var(--muted)}
.gray-btn{left:48px;top:1125px;width:264px;height:30px;background:linear-gradient(#eee,#c8c8c8);border:1px solid #bbb;border-radius:5px;font-family:"Roboto Condensed",sans-serif;font-size:13px;color:#444;text-align:center;line-height:28px;text-transform:uppercase}
.videos{left:360px;top:892px;width:280px}
.player{left:360px;top:940px;width:279px;height:200px;background:linear-gradient(#cfcfcf,#8e8e8e);border:1px solid #777;padding:9px}
.screen{width:100%;height:155px;background:radial-gradient(ellipse at 50% 40%,#1e3a1a,#000 80%);display:flex;flex-direction:column;justify-content:center;padding-left:28px;color:var(--white)}
.screen .n{font-size:30px;line-height:30px}
.screen .s{font-size:19px;line-height:19px}
.screen .g{font-size:15px;color:var(--green-light)}
.controls{height:26px;background:linear-gradient(#eee,#b5b5b5);display:flex;align-items:center;gap:8px;padding:0 6px;font-size:11px;color:#333}
.track{flex:1;height:6px;background:#888;border-radius:3px}
.downloads{left:683px;top:892px;width:277px}
.dl-box{left:688px;top:947px;width:263px;height:189px;background:#f8fbfd;border:3px solid #d6d6d6}
.dl-art{position:absolute;left:62px;top:5px;width:140px;height:176px;background:linear-gradient(#f4f7fa 0%,#e8eff6 45%,#3d88c8 75%,#11548f)}
.dl-arrow{position:absolute;top:82px;width:20px;height:22px;background:#bbb;display:flex;align-items:center;justify-content:center}
.footer{left:0;top:1178px;width:1000px;text-align:center;font-size:12px;color:#333}
.footer .links{margin-top:11px;color:var(--link)}
</style>
</head>
<body>
<div class="page">
  <div class="abs header-bg"></div>

  <div class="abs nav">
    <svg class="abs" style="left:0;top:6px" width="1000" height="52" aria-hidden="true">
      <polygon points="0,0 22,0 22,38 12,52 12,38" fill="#2b7510"/>
      <polygon points="1000,0 978,0 978,38 988,52 988,38" fill="#2b7510"/>
    </svg>
    <div class="abs nav-bar"></div>
    <ul>
      <li class="active">Home</li><li>Features</li><li>Plugins</li><li>Tutorials</li><li>Fltcnsl</li>
    </ul>
  </div>

  <div class="abs logo">
    <div class="logo-name">PLORN.IE</div>
    <div class="logo-sub">Fleet Console</div>
    <div class="logo-sub green">User Group Ireland</div>
    <div class="abs logo-mark"></div>
  </div>

  <div class="abs account"><span>Log in</span><span>Sign Up</span></div>
  <div class="abs phone">
    <svg width="26" height="26" viewBox="0 0 26 26" aria-hidden="true"><circle cx="13" cy="13" r="12" fill="none" stroke="#aaa" stroke-width="2"/><path d="M9 7l3 3-2 2c1 2 2 3 4 4l2-2 3 3-2 2c-5 0-10-5-10-10z" fill="#aaa"/></svg>
    0123 456 789
  </div>
  <div class="abs search">Search here...
    <svg width="12" height="12" viewBox="0 0 12 12" aria-hidden="true"><circle cx="5" cy="5" r="3.5" fill="none" stroke="#aaa" stroke-width="1.5"/><line x1="7.5" y1="7.5" x2="11" y2="11" stroke="#aaa" stroke-width="2"/></svg>
  </div>

  <div class="abs slider"><div class="slider-photo" role="img" aria-label="Photo of three colleagues laughing in front of a server rack"></div></div>
  <div class="abs arrow" style="left:20px;top:281px"><svg width="10" height="12" aria-hidden="true"><polygon points="9,0 9,12 1,6" fill="#555"/></svg></div>
  <div class="abs arrow" style="left:933px;top:281px"><svg width="10" height="12" aria-hidden="true"><polygon points="1,0 1,12 9,6" fill="#555"/></svg></div>

  <div class="abs cards">
    <div class="card" style="left:0"><div class="card-photo" role="img" aria-label="Photo of a team meeting"></div><h3>EXPLORE</h3><div class="sub">Fleet<br>Console</div><p>Lorem ipsum dolor amet,</p><a>Read more</a></div>
    <div class="card" style="left:225px"><div class="card-photo" role="img" aria-label="Photo of a planning discussion"></div><h3>PLAN</h3><div class="sub">Fleet<br>Console</div><p>Lorem ipsum dolor amet,</p><a>Read more</a></div>
    <div class="card" style="left:450px"><div class="card-photo" role="img" aria-label="Photo of an engineer in a data centre"></div><h3>DEPLOY</h3><div class="sub">Fleet<br>Console</div><p>Lorem ipsum dolor amet,</p><a>Read more</a></div>
    <div class="card" style="left:675px"><div class="card-photo" role="img" aria-label="Photo of network cables being connected"></div><h3>CONFIGURE</h3><div class="sub">Fleet<br>Console</div><p>Lorem ipsum dolor amet,</p><a>Read more</a></div>
  </div>

  <div class="abs news">
    <svg class="abs" style="left:0;top:0" width="36" height="36" viewBox="0 0 36 36" aria-hidden="true"><rect x="2" y="6" width="32" height="28" rx="2" fill="none" stroke="#5aaa2a" stroke-width="3"/><rect x="2" y="6" width="32" height="9" fill="#5aaa2a"/><rect x="8" y="1" width="4" height="9" fill="#5aaa2a"/><rect x="24" y="1" width="4" height="9" fill="#5aaa2a"/></svg>
    <p><b>Lorem ipsum dolor sit amet,</b> Lorem ipsum dolor sit amet, consectetur adipiscing elit. Morbi eu accumsan nisl. In pellentesque gravida arcu, sit amet euismod massa venenatis posuerenon dolores quos hic incididunt, nam facilisi?</p>
    <p><b>Lorem ipsum dolor sit amet,</b> Lorem ipsum dolor sit amet, consectetur adipiscing elit. Morbi eu accumsan nisl. In pellentesque gravida arcu, sit amet euismod massa venenatis posuerenon dolores quos hic incididunt, dolor sit amet, nam facilisi?</p>
    <span class="btn" style="margin-left:53px;width:165px;height:25px;line-height:23px">View all news &amp; events</span>
  </div>

  <div class="abs demo">
    <h2>Demo Information</h2>
    <div class="quote">“Lorem ipsum dolor sit amet, consectetur adipiscing elit. Morbi eu accumsan nisl. In pellentesque gravida arcu”</div>
    <p>Lorem ipsum dolor sit amet, consectetur adipiscing elit. Morbi eu accumsan nisl. In pellentesque gravida arcu, sit amet euismod massa venenatis Lorem ipsum dolor sit amet posuere.</p>
    <span class="btn" style="margin-top:20px;width:96px;height:25px;line-height:23px">Learn more</span>
  </div>

  <div class="abs band"></div>

  <div class="abs blogs">
    <div class="col-head"><svg width="34" height="34" viewBox="0 0 34 34" aria-hidden="true"><circle cx="17" cy="17" r="16" fill="#ee7a1c"/><circle cx="11" cy="23" r="3" fill="#fff"/><path d="M8 14a12 12 0 0 1 12 12M8 8a18 18 0 0 1 18 18" fill="none" stroke="#fff" stroke-width="3"/></svg>Blogs</div>
    <div class="blog-item"><div class="avatar"></div><div><b>Lorem ipsum</b><span>Lorem ipsum dolor sit amet,</span></div></div>
    <div class="blog-item"><div class="avatar"></div><div><b>Lorem ipsum</b><span>Lorem ipsum dolor sit amet,</span></div></div>
    <div class="blog-item"><div class="avatar"></div><div><b>Lorem ipsum</b><span>Lorem ipsum dolor sit amet,</span></div></div>
    <div class="blog-item"><div class="avatar"></div><div><b>Lorem ipsum</b><span>Lorem ipsum dolor sit amet,</span></div></div>
  </div>
  <div class="abs gray-btn">Learn more</div>

  <div class="abs videos">
    <div class="col-head"><svg width="32" height="30" aria-hidden="true"><rect x="1" y="1" width="30" height="28" rx="5" fill="#c8231b"/></svg>Videos</div>
  </div>
  <div class="abs player">
    <div class="screen">
      <div class="n">PLORN.IE</div><div class="s">Fleet Console</div><div class="g">User Group Ireland</div>
    </div>
    <div class="controls">
      <svg width="14" height="14" aria-hidden="true"><polygon points="2,1 13,7 2,13" fill="#333"/></svg>
      <svg width="16" height="14" aria-hidden="true"><polygon points="1,5 5,5 9,1 9,13 5,9 1,9" fill="#333"/></svg>
      <span>0:00 / 0:00</span><div class="track"></div>
      <svg width="14" height="14" aria-hidden="true"><path d="M1 5V1h4M13 5V1H9M1 9v4h4M13 9v4H9" fill="none" stroke="#333" stroke-width="2"/></svg>
    </div>
  </div>

  <div class="abs downloads">
    <div class="col-head"><svg width="34" height="34" viewBox="0 0 34 34" aria-hidden="true"><rect x="3" y="4" width="24" height="28" rx="2" fill="#7a7a7a"/><rect x="7" y="8" width="16" height="10" fill="#ddd"/><circle cx="26" cy="24" r="8" fill="#4caf27"/><path d="M26 19v8M22 24l4 4 4-4" fill="none" stroke="#fff" stroke-width="2"/></svg>Download Section</div>
  </div>
  <div class="abs dl-box">
    <div class="dl-art" role="img" aria-label="Download cover artwork showing splashing water"></div>
    <div class="dl-arrow" style="left:0"><svg width="10" height="12" aria-hidden="true"><polygon points="1,0 1,12 9,6" fill="#fff"/></svg></div>
    <div class="dl-arrow" style="right:0"><svg width="10" height="12" aria-hidden="true"><polygon points="9,0 9,12 1,6" fill="#fff"/></svg></div>
  </div>

  <div class="abs footer">
    <div>© 2012-2013 Plorn.ie Fleet Console User Group Ireland, all rights reserved.</div>
    <div class="links">Contact Us | Disclaimer | Site Map</div>
  </div>
</div>
</body>
</html>
```